Water Delivery Service Website

We are working with BrivoneÉ. They are a water delivery company and in need of a new website design.
Some sites to use for inspiration:
https://www.tesmoracrest.example/home
https://www.plimvarta.example/en/home3
https://www.quelbo.example
https://www.fandorix.example
Thank you for taking the time to consider designing a website for us. We are web developers based in Stockton, CA, USA. Most of our projects go through the same process. Understanding this process may help you win a project with us. We custom-code all of our websites in-house. We don’t have any requirements as to what tools you use for your design, but we prefer Figma files. For any design that we label as four-stars, we send it to the client for review. The client picks the final design they want us to use. Once we complete this process, we will continue to show additional clients all the four-star sites and purchase them later. Your designs will have multiple chances to sell. For better chances of success, we ask that you follow these guidelines.
IMAGES:
If you use any images or icons in the design, we ask that you have a link to the asset so we can purchase the image/icon. Most of the designs we submit do not have the customer’s images on them unless they have some great images. Be creative; show us the feeling you are trying to portray with your image choices. Use any royalty-free site you choose. We subscribe to Adobe and mainly use their images, but we can purchase images outside of Adobe.
PLEASE NOTE: we will not submit designs to clients with watermarks on the images.
FONTS:
We ask that you identify the fonts used in the design. This can be done in a message if you want. We typically use Google Fonts and Adobe Fonts.
CONTENT:
We're always open to different content and ideas. We often submit designs with stock images so the client can see our vision. We typically take pictures after the website launch to use their images with our vision. Lorem Ipsum is fine for paragraphs, but we ask that you write the headers in correct English. We want to be able to show the vision and identify the sections of the website.
INSPIRATION:
We typically add a couple of links in the brief of websites we like to help you get started in your design.
REVISIONS:
We do not often ask for revisions of the designs unless we see something in the design that may not appeal to the client. If there are slight changes that we want to make, we do that in the development process.
FEEDBACK:
We rarely give feedback on designs during the design process. We are working on many website projects and do not have the time to provide feedback. We usually respond if your request is well thought out and asks specific questions, but a note asking “feedback, please” usually goes unanswered.

```html
<!DOCTYPE html>
<html lang="en">
<head>
<meta charset="utf-8">
<title>BrivoneÉ — Water Delivery</title>
<link href="https://fonts.googleapis.com/css2?family=Inter:wght@400;500;600;700;800&display=swap" rel="stylesheet">
<style>
:root{
  --blue:#1f5fcf;
  --blue-dark:#1c3f9e;
  --sky:#17a6e8;
  --cyan:#23d3f0;
  --magenta:#e82ad6;
  --purple:#a34bd8;
  --ink:#1b2a44;
  --muted:#6b7891;
  --pale:#eaf6fd;
  --card-line:#cfe6f7;
  --star:#f6b80b;
  --footer:#1a5fd0;
}
*{margin:0;padding:0;box-sizing:border-box}
html,body{width:1200px;height:5112px;overflow:hidden}
body{position:relative;font-family:'Inter',sans-serif;color:var(--ink);background:#fff}
.abs{position:absolute}
.band{position:absolute;left:0;width:1200px}
.brand{font-family:'Inter',sans-serif;font-weight:500;color:var(--blue);display:flex;align-items:center;gap:8px}
.brand .dot{width:14px;height:14px;border-radius:50%;background:var(--blue)}
.nav a{position:absolute;top:60px;font-size:13px;color:var(--blue);text-decoration:none;font-weight:500}
.grad-btn{position:absolute;display:flex;align-items:center;justify-content:center;gap:10px;color:#fff;font-weight:600;font-size:14px;letter-spacing:.5px;border-radius:22px;background:linear-gradient(90deg,var(--magenta),var(--blue))}
.photo{position:absolute}
.feature{position:absolute;top:862px;width:226px;height:418px;border-radius:18px;background:linear-gradient(180deg,#cfeefd 0%,#fff 55%);border:1px solid var(--card-line);box-shadow:0 8px 18px rgba(31,95,207,.12);text-align:center}
.feature .ring{width:126px;height:126px;border-radius:50%;margin:26px auto 0;background:#bfe4fa;display:flex;align-items:center;justify-content:center}
.feature .ring div{width:104px;height:104px;border-radius:50%;background:linear-gradient(135deg,#1fa0ea,#1f5fcf);border:3px solid #fff;display:flex;align-items:center;justify-content:center}
.feature h3{margin-top:34px;font-size:20px;color:var(--purple);font-weight:600}
.feature p{margin:20px auto 0;width:162px;text-align:left;font-size:11.5px;line-height:18px;color:var(--muted)}
.feature .more{position:absolute;bottom:22px;left:0;right:0;font-size:13px;font-weight:600;color:var(--blue)}
.tab{position:absolute;top:1632px;font-size:15px;font-weight:500;line-height:19px}
.prod{position:absolute;top:1725px;width:266px;height:260px;background:#fff;border-radius:14px;box-shadow:0 6px 16px rgba(31,95,207,.12)}
.prod .pic{position:absolute;left:40px;top:16px;width:186px;height:180px;border-radius:10px;background:linear-gradient(180deg,#e5f3fd,#a7d6f6)}
.prod .more{position:absolute;right:30px;bottom:22px;font-size:13px;color:var(--muted);font-weight:500}
.arrow{position:absolute;width:32px;height:32px;border-radius:50%;background:#fff;box-shadow:0 2px 8px rgba(0,0,0,.15);display:flex;align-items:center;justify-content:center;font-size:16px;color:var(--ink)}
.check{position:absolute;left:520px;width:490px;font-size:15px;color:var(--ink);padding-left:42px;border-bottom:1px solid #c8d2df;padding-bottom:8px;line-height:20px}
.check::before{content:"✓";position:absolute;left:0;top:0;width:20px;height:20px;border-radius:50%;background:var(--blue-dark);color:#fff;font-size:12px;text-align:center;line-height:20px}
.plan{position:absolute;border:4px solid var(--cyan);border-radius:8px;background:linear-gradient(180deg,#fff,#eef9fe);text-align:center;box-shadow:0 0 0 3px #d8f3fb}
.plan h3{font-size:25px;color:var(--blue-dark);font-weight:800}
.plan .sub{font-size:7.5px;color:var(--muted);margin-top:4px}
.plan .price{font-size:38px;color:var(--ink);font-weight:500;margin-top:14px}
.plan .price sup{font-size:16px;vertical-align:top;position:relative;top:6px}
.plan .note{font-size:8px;color:var(--muted)}
.plan ul{list-style:none;text-align:left;margin:30px 0 0 36px}
.plan li{position:relative;font-size:10px;font-weight:600;color:var(--blue-dark);padding-left:22px;margin-bottom:14px;line-height:13px}
.plan li::before{content:"✓";position:absolute;left:0;top:-1px;width:13px;height:13px;border-radius:50%;background:var(--blue-dark);color:#fff;font-size:8px;text-align:center;line-height:13px}
.why{position:absolute;width:240px;left:190px;text-align:center}
.why h4{font-size:19px;color:var(--blue);font-weight:600;line-height:26px}
.why p{font-size:15px;color:var(--ink);line-height:22px;margin-top:14px}
.tdot{position:absolute;left:467px;width:30px;height:30px;border-radius:50%}
.review{position:absolute;top:4430px;width:360px;text-align:center}
.review .avatar{position:absolute;left:0;top:0;width:80px;height:80px;border-radius:50%;background:#d9d9d9}
.review .name{position:absolute;left:100px;top:6px;font-size:24px;color:var(--ink)}
.review .stars{position:absolute;left:100px;top:42px;font-size:17px;color:var(--star);letter-spacing:6px}
.review .stars span{font-size:11px;color:var(--muted);letter-spacing:0;margin-left:6px}
.review p{position:absolute;top:108px;left:-40px;width:400px;font-size:15.5px;line-height:26px;color:var(--blue)}
.footer{top:4730px;height:382px;background:var(--footer);color:#fff}
.footer h5{position:absolute;top:105px;font-size:18px;font-weight:600}
.footer ul{position:absolute;top:150px;list-style:none;font-size:12px;line-height:32px}
</style>
</head>
<body>

<!-- Header -->
<div class="band" style="top:0;height:116px;background:#f2f9fe;border-bottom:1px solid #e0ecf5"></div>
<div class="brand abs" style="left:125px;top:44px;font-size:30px"><span class="dot"></span>BrivoneÉ</div>
<nav class="nav">
  <a style="left:400px">Home</a><a style="left:487px">Services</a><a style="left:599px">Products</a><a style="left:715px">About Us</a>
</nav>
<div class="abs" style="left:882px;top:50px;font-size:12px;color:var(--blue)">Contact Us</div>
<div class="abs" style="left:882px;top:70px;font-size:20px;font-weight:700;background:linear-gradient(90deg,var(--blue-dark),var(--magenta));-webkit-background-clip:text;background-clip:text;color:transparent">000 123 456 789</div>

<!-- Hero -->
<div class="band" style="top:117px;height:700px;background:linear-gradient(180deg,#f4fafe,#fff)"></div>
<div class="abs" style="left:160px;top:164px;font-size:20px;color:var(--star);letter-spacing:8px">★★★★★</div>
<h1 class="abs" style="left:159px;top:194px;width:420px;font-size:40px;line-height:45px;font-weight:700;color:var(--blue-dark)">We ensure that you receive the <span style="color:var(--sky)">highest quality water</span></h1>
<div class="abs" style="left:159px;top:340px;font-size:30px;color:var(--purple)">right at your doorstep.</div>
<div class="abs" style="left:159px;top:409px;width:380px;height:250px;border:1px solid var(--blue);background:#fff"></div>
<div class="abs" style="left:182px;top:438px;width:334px;height:32px;border:1px solid #9fb2cc;font-size:12px;color:#9aa6b8;padding:8px 10px">Name...</div>
<div class="abs" style="left:182px;top:481px;width:334px;height:32px;border:1px solid #9fb2cc;font-size:12px;color:#9aa6b8;padding:8px 10px">Address...</div>
<div class="abs" style="left:182px;top:524px;width:334px;height:32px;border:1px solid #9fb2cc;font-size:12px;color:#9aa6b8;padding:8px 10px">Phone Number...</div>
<div class="abs" style="left:182px;top:567px;width:334px;height:32px;border:1px solid #9fb2cc;font-size:12px;color:#9aa6b8;padding:8px 10px">Bottles...</div>
<div class="grad-btn" style="left:182px;top:618px;width:334px;height:34px;border-radius:2px;font-size:13px">Place The Order</div>
<div class="abs" style="left:159px;top:715px;font-size:15px;font-weight:600;color:var(--blue-dark)">Contact us or place your order online now!</div>
<div class="photo" role="img" aria-label="Three large blue water bottles with a splash of water" style="left:640px;top:190px;width:430px;height:560px;border-radius:40%;background:radial-gradient(ellipse at center,#9fd3f6 0%,#cdeafc 55%,#fff 75%)"></div>

<!-- Water types -->
<div class="feature" style="left:142px"><div class="ring"><div><svg width="50" height="50" viewBox="0 0 50 50" fill="none" stroke="#fff" stroke-width="2.5"><rect x="9" y="10" width="9" height="30" rx="2"/><rect x="21" y="10" width="9" height="30" rx="2"/><rect x="33" y="10" width="9" height="30" rx="2"/><path d="M5 25h40"/></svg></div></div><h3>Purified</h3><p>Enjoy the crisp, clean taste of purified water. Purified water is filtered to remove impurities like chemicals and other contaminants for pure refreshment</p><div class="more">More ›</div></div>
<div class="feature" style="left:379px"><div class="ring"><div><svg width="50" height="50" viewBox="0 0 50 50" fill="none" stroke="#fff" stroke-width="2.5"><path d="M25 6C18 17 12 24 12 31a13 13 0 0 0 26 0c0-7-6-14-13-25z"/><path d="M20 33l10-10"/></svg></div></div><h3>Spring</h3><p>Crisp, pure, and refreshing. Spring water comes from an underground formation and is collected at its source and bottled for your enjoyment.</p><div class="more">More ›</div></div>
<div class="feature" style="left:615px"><div class="ring"><div><svg width="50" height="50" viewBox="0 0 50 50" fill="none" stroke="#fff" stroke-width="2.5"><path d="M25 6l16 6v12c0 10-7 17-16 20C16 41 9 34 9 24V12z"/><path d="M25 16c-4 6-7 9-7 13a7 7 0 0 0 14 0c0-4-3-7-7-13z"/></svg></div></div><h3>Alkaline</h3><p>Velora Water Plus is a purified water enhanced with minerals for a smooth taste and a pH level of 9.5 at the time of bottling.</p><div class="more">More ›</div></div>
<div class="feature" style="left:852px"><div class="ring"><div><svg width="50" height="50" viewBox="0 0 50 50" fill="none" stroke="#fff" stroke-width="2.5"><circle cx="25" cy="20" r="9"/><path d="M25 5v5M25 30v5M10 20h5M35 20h5"/><path d="M8 40c6-4 12-4 17-1s11 3 17-1"/></svg></div></div><h3>Distilled</h3><p>Crestwell distilled water is boiled to remove all impurities, reducing water to its purest form, H2O.</p><div class="more">More ›</div></div>

<!-- Products & Services -->
<div class="band" style="top:1418px;height:1022px;background:linear-gradient(180deg,#e9f5fd,#fff 20%,#fff 85%,#eef8fe)"></div>
<div class="photo" role="img" aria-label="Delivery worker in blue overalls carrying a water bottle, with two large bottles at her feet" style="left:100px;top:1480px;width:340px;height:895px;border-radius:30px;background:linear-gradient(180deg,#dbeefb,#2a58c8 40%,#c7e4f8 80%,#eaf5fd)"></div>
<h2 class="abs" style="left:495px;top:1508px;font-size:38px;font-weight:500;color:var(--blue)">Our Products &amp; Services</h2>
<div class="tab" style="left:476px;color:var(--blue-dark)">Filtration Systems<br>&amp; Dispensers</div>
<div class="abs" style="left:645px;top:1638px;width:1px;height:34px;background:#333"></div>
<div class="tab" style="left:679px;color:var(--magenta)">Bottled Water<br>Delivery</div>
<div class="abs" style="left:818px;top:1638px;width:1px;height:34px;background:var(--magenta)"></div>
<div class="tab" style="left:840px;color:var(--blue-dark)">Bulk &amp; Commercial<br>Water Supply</div>
<div class="abs" style="left:1024px;top:1636px;width:5px;font-size:20px;line-height:9px;color:#777">·<br>·<br>·</div>
<div class="prod" style="left:465px"><div class="pic" role="img" aria-label="Three small bottles of water"></div><div class="more">More ›</div></div>
<div class="prod" style="left:738px"><div class="pic" role="img" aria-label="Two large water jugs"></div><div class="more">More ›</div></div>
<div class="arrow" style="left:414px;top:1827px">‹</div>
<div class="arrow" style="left:1017px;top:1827px">›</div>
<h3 class="abs" style="left:0;width:1502px;text-align:center;top:2026px;font-size:25px;font-weight:600;color:var(--blue-dark)">Bottled Water Delivery</h3>
<p class="abs" style="left:500px;width:502px;top:2072px;text-align:center;font-size:12.5px;line-height:20px;color:var(--blue)">Lorem ipsum dolor sit amet consectetur adipiscing elit Ut et massa mi. Aliquam in hendrerit urna. Pellentesque sit amet sapien fringilla, mattis ligula consectetur, ultrices mauris.</p>
<div class="check" style="top:2158px">Ideal for homes and offices, available in purified,<br>spring, and alkaline options.</div>
<div class="check" style="top:2218px">Perfect for small families and personal use.</div>
<div class="grad-btn" style="left:645px;top:2282px;width:202px;height:42px">BUY NOW <span style="width:18px;height:18px;border:2px solid #fff;border-radius:50%;font-size:10px;display:flex;align-items:center;justify-content:center">›</span></div>

<!-- Pricing -->
<div class="band" style="top:2440px;height:1000px;background:linear-gradient(180deg,#fff,#e4f3fc)"></div>
<h2 class="abs" style="left:0;width:1200px;text-align:center;top:2520px;font-size:40px;font-weight:500;color:var(--blue)">Choose Your Pricing Plan</h2>
<div class="plan" style="left:193px;top:2665px;width:257px;height:350px;padding-top:28px"><h3>Basic</h3><div class="sub">(Small Family or Minimal Usage)</div><div class="price"><sup>$</sup>90</div><div class="note">(depending on the bottle type)</div><ul><li>Ideal for: 2-3 people</li><li>~2 gallons per person per day</li><li>Monthly Supply<br>5-Gallon Bottles: 10-12<br>1-Gallon Bottles: 30-35<br>16.9 oz Bottles: 150-200</li></ul></div>
<div class="plan" style="left:464px;top:2640px;width:256px;height:400px;padding-top:52px;background:linear-gradient(180deg,#d6f1fd,#c8ebfb);overflow:hidden"><div class="abs" style="right:-40px;top:26px;width:190px;transform:rotate(45deg);background:#d9d9d9;font-size:7px;color:#fff;padding:4px 0">Recommended</div><h3>Standard</h3><div class="sub">(Medium Family or Regular Usage)</div><div class="price"><sup>$</sup>110</div><div class="note">(depending on the bottle type)</div><ul><li>Ideal for: 4-5 people</li><li>~2.5 gallons per person per day</li><li>Monthly Supply<br>5-Gallon Bottles: 15-18<br>1-Gallon Bottles: 45-50<br>16.9 oz Bottles: 250-300</li></ul></div>
<div class="plan" style="left:736px;top:2665px;width:256px;height:350px;padding-top:28px"><h3>Premium</h3><div class="sub">(Large Family or High Usage)</div><div class="price"><sup>$</sup>150</div><div class="note">(depending on the bottle type)</div><ul><li>Ideal for: 6+ people</li><li>~3 gallons per person per day</li><li>Monthly Supply<br>5-Gallon Bottles: 20-25<br>1-Gallon Bottles: 60-70<br>16.9 oz Bottles: 350-400</li></ul></div>
<div class="abs" style="left:0;width:1200px;text-align:center;top:3096px;font-size:30px;line-height:38px;font-weight:600;color:var(--blue-dark)">Experience the convenience of fresh, pure<br>water delivered to you</div>
<div class="abs" style="left:0;width:1200px;text-align:center;top:3186px;font-size:33px;line-height:38px;font-weight:700;background:linear-gradient(90deg,var(--magenta) 35%,var(--blue-dark) 65%);-webkit-background-clip:text;background-clip:text;color:transparent">Contact us or place your order<br>online now!</div>
<div class="grad-btn" style="left:497px;top:3287px;width:201px;height:42px">MY ORDER <span style="width:18px;height:18px;border:2px solid #fff;border-radius:50%;font-size:10px;display:flex;align-items:center;justify-content:center">›</span></div>

<!-- Why choose us -->
<div class="band" style="top:3440px;height:1290px;background:linear-gradient(180deg,#fff,#f3f9fe 50%,#fff)"></div>
<div class="abs" style="left:481px;top:3530px;width:2px;height:590px;background:var(--blue-dark)"></div>
<div class="tdot" style="top:3607px;background:var(--magenta)"></div>
<div class="tdot" style="top:3801px;background:var(--blue)"></div>
<div class="tdot" style="top:4000px;background:var(--cyan)"></div>
<div class="why" style="top:3556px"><h4>High-Quality,<br>Purified Water</h4><p>We use state-of-the-art filtration to ensure purity and great taste.</p></div>
<div class="why" style="top:3770px"><h4>Reliable &amp; Timely<br>Delivery</h4><p>Never run out of water with our scheduled deliveries.</p></div>
<div class="why" style="top:3980px"><h4>Affordable Pricing</h4><p>Competitive rates with flexible payment options.</p></div>
<div class="brand abs" style="left:668px;top:3535px;font-size:42px"><span class="dot" style="width:20px;height:20px"></span>BrivoneÉ</div>
<div class="abs" style="left:570px;top:3605px;width:430px;height:430px;border-radius:50%;background:#c9d8f3"></div>
<div class="photo" role="img" aria-label="Delivery man in a blue cap and shirt carrying a water bottle on his shoulder" style="left:600px;top:3635px;width:370px;height:370px;border-radius:50%;background:linear-gradient(180deg,#3d7de0,#1a49b5)"></div>

<!-- Testimonials -->
<h2 class="abs" style="left:0;width:1200px;text-align:center;top:4300px;font-size:38px;font-weight:500;color:var(--blue)">What Our Client says</h2>
<div class="abs" style="left:156px;top:4494px;font-size:22px;color:var(--ink)">‹</div>
<div class="abs" style="left:1016px;top:4494px;font-size:22px;color:var(--ink)">›</div>
<div class="review" style="left:245px"><div class="avatar"></div><div class="name">Mira Castell</div><div class="stars">★★★★★<span>5.0</span></div><p>Lorem ipsum dolor sit amet consectetur adipiscing elit Ut et massa mi. Aliquam in hendrerit urna. Pellentesque sit amet sapien fringilla, mattis ligula consectetur</p></div>
<div class="review" style="left:665px"><div class="avatar"></div><div class="name">Devon Rhys</div><div class="stars">★★★★★<span>5.0</span></div><p>Lorem ipsum dolor sit amet consectetur adipiscing elit Ut et massa mi. Aliquam in hendrerit urna. Pellentesque sit amet sapien fringilla, mattis ligula</p></div>

<!-- Footer -->
<footer class="band footer">
  <div class="brand abs" style="left:140px;top:100px;font-size:28px;color:#fff"><span class="dot" style="background:#fff"></span>BrivoneÉ</div>
  <p class="abs" style="left:140px;top:150px;width:300px;font-size:9px;line-height:13px;color:#dfe8fb">Lorem ipsum dolor sit amet consectetur adipiscing elit Ut et massa mi. Aliquam in hendrerit urna. Pellentesque sit amet sapien fringilla, mattis ligula consectetur, ultrices mauris. Maecenas vitae mattis tellus. Nullam quis imperdiet augue. Vestibulum auctor ornare leo, non</p>
  <div class="abs" style="left:140px;top:236px;display:flex;gap:10px">
    <span style="width:14px;height:14px;border-radius:50%;background:#fff"></span><span style="width:14px;height:14px;border-radius:50%;background:#fff"></span><span style="width:14px;height:14px;border-radius:50%;background:#fff"></span><span style="width:14px;height:14px;border-radius:50%;background:#fff"></span><span style="width:14px;height:14px;border-radius:50%;background:#fff"></span>
  </div>
  <h5 style="left:508px">Company</h5>
  <ul style="left:510px"><li>About Us</li><li>Our Services</li><li>Our Prices</li><li>Our Products</li></ul>
  <h5 style="left:655px">Resources</h5>
  <ul style="left:657px"><li>Water Quality</li><li>Water Purify Methods</li><li>Blog</li><li>Other Sources</li></ul>
  <h5 style="left:845px">Subscribe</h5>
  <div class="abs" style="left:845px;top:125px;width:192px;height:37px;border-radius:19px;background:#fff"></div>
  <div class="abs" style="left:940px;top:180px;width:97px;height:26px;border-radius:13px;background:#fff;color:var(--blue);font-size:10px;text-align:center;line-height:26px">Subscribe</div>
  <div class="abs" style="left:140px;top:265px;width:920px;height:1px;background:#6d97e3"></div>
  <div class="abs" style="left:775px;top:285px;font-size:10px;display:flex;gap:30px"><span>Terms of Use</span><span>Privacy Policy</span><span>Cookie Policy</span></div>
</footer>
</body>
</html>
```